Billboard Design: Helicopter + Tampa/St. Pete Beach Composite (5 Variations)

We are looking for a skilled graphic designer to create five (5) high impact billboard designs using the provided helicopter photos and Tampa/St. Pete Beach background photos. The helicopter images were NOT taken over Tampa, so the designer must realistically composite the helicopter and Feet POV into the Tampa skyline scenes. The final images must look authentic, natural, and professionally blended, not like a cheap Photoshop cutout. These designs will be used for a real billboard advertising campaign, so realism and visual impact are essential.

***Zorvane Link to download high-resolution photos:***
https://files.marnetbox.com/share/7qzLw2RkT9xBv4NcHd8PyE3sMa6Ju0FgQ?src=link

Required Scenes (5 Total):
1. Tampa Skyline + Helicopter Front
2. Tampa Skyline + Helicopter Side Door (facing backwards)
3. Tampa Skyline + Feet POV
4. Beach Background + Helicopter Front (You can use the Beach/Helicopter picture as provided since that photo was taken in the correct scene)
5. Beach Background + Helicopter Front (You can use the Beach/Helicopter picture as provided since that photo was taken in the correct scene)
Some designs must include the feet outside POV image.

Each Billboard Must Include:
• One catch phrase (assigned below)
• One discount phrase + discount code
• Our logo
• Our website: www.hoverquill.com
• A realistic composite of:
o Helicopter
o Leg out POV
o Beach background

Catch Phrase + Discount Code Assignments:
1. Adventure Starts Here.
Use Code CORAL25 for $25 Off

2. See Tampa From Above.
Take $25 Off with Code UP25

3. Elevate Your Weekend.
Use Code YES25 for $25 Off

4. The Ultimate Date Night.
Take $25 Off with Code LOVE25

5. Sunset Hits Different.
Use Code SUNSET25 for $25 Off

6. Premium Views. No Filter.
Take $25 Off with Code SKY25

7. Bucket List? Check.

(You will design five billboards, but these seven options are provided so you can choose the strongest matches for each scene.)

Deliverables:
• Five (5) billboard ready designs
• High resolution JPEG files in the exact required pixel dimensions
• Layered PSD files for future edits
• Consistent branding across all designs

Important Notes:
• The helicopter must look like it belongs in the scene. Correct lighting, shadows, and scale are essential.
• Designs should feel premium, exciting, and tourism oriented.
• This project is for a real billboard campaign, so quality must be top tier.

Billboard Specifications:
(IMPORTANT — MUST FOLLOW EXACTLY)
Your final artwork must match the exact pixel dimensions required by the billboard units. These are absolute pixel sizes and must be delivered 1:1 — no scaling, no DPI adjustments.

Billboard Size Option 1: 14' x 48' Digital Bulletin
• Display Resolution: 208 px (height) × 720 px (width)
• Mechanical/Artwork Size: 208 px × 720 px
• File Format: JPEG
• Color Mode: sRGB
• Bright white backgrounds are discouraged; if used, target R235 / G235 / B235 (“broadcast safe white”).
• File must be delivered at exact resolution (1:1 pixel ratio).

Billboard Size Option 2: 10'6" x 36' Digital Bulletin
• Display Resolution: 160 px (height) × 544 px (width)
• Mechanical/Artwork Size: 160 px × 544 px
• File Format: JPEG
• Color Mode: sRGB
• Same broadcast safe white recommendation applies.
• Must be delivered at exact resolution (1:1 pixel ratio).
Designers may create layouts for either size, but the final deliverables must be exported in the correct pixel dimensions for the selected unit.

Target Market(s)

Our billboards are aimed at tourists, couples, families, and locals looking for memorable experiences in Tampa and St. Pete. The audience includes visitors seeking unique aerial views, couples planning romantic outings, adventure‑seekers wanting something exciting and scenic, and social‑media‑driven customers who value visually striking, Instagram‑worthy moments.

Requirements
Must have
• The final designs must include photorealistic compositing of our helicopter into Tampa skyline or beach backgrounds, with lighting, shadows, and scale that look completely authentic. Designers must deliver artwork in the exact required pixel dimensions for the billboard units, using clean, bold typography that remains readable from a distance. Each design must include a catch phrase, a discount phrase with its code, our logo, and our website URL, and all files must be delivered as layered PSDs along with high‑resolution JPEGs.
Nice to have
• It is helpful if designers incorporate subtle atmospheric effects such as haze, color grading, or lighting adjustments to enhance realism and mood. Creative depth, perspective, or motion can make the helicopter feel more dynamic, and slight variations in tone or style across the five designs are welcome. Including the feet‑out POV image where it naturally fits the composition is also a plus.

```html
<!DOCTYPE html>
<html lang="en">
<head>
<meta charset="utf-8">
<title>HoverQuill Billboard – Bucket List? Check.</title>
<link rel="stylesheet" href="https://fonts.googleapis.com/css2?family=Anton&family=Archivo+Black&family=Oswald:wght@600&family=Michroma&display=swap">
<style>
  :root {
    --stage: #c4c4c4;
    --sky-top: #8fc3ea;
    --sky-mid: #d9e6f1;
    --cloud: #f3ece4;
    --cloud-warm: #f6dcc0;
    --brand-blue: #1668d8;
    --brand-blue-deep: #0d4fb8;
    --brand-blue-light: #2f8af0;
    --promo-red: #e0262f;
    --promo-red-deep: #b5121b;
    --ink: #111111;
    --white: #ffffff;
  }
  * { margin: 0; padding: 0; box-sizing: border-box; }
  html, body {
    width: 1200px; height: 488px; overflow: hidden;
    background: var(--stage);
  }
  .billboard {
    position: absolute; left: 72px; top: 88px;
    width: 1058px; height: 311px; overflow: hidden;
  }
  .sky-backdrop {
    position: absolute; inset: 0;
    background:
      radial-gradient(ellipse 60% 45% at 20% 90%, var(--cloud) 0%, transparent 70%),
      radial-gradient(ellipse 50% 30% at 15% 55%, var(--cloud-warm) 0%, transparent 70%),
      linear-gradient(180deg, var(--sky-mid) 0%, var(--sky-top) 35%, var(--sky-mid) 60%, var(--cloud) 100%);
  }
  .aerial-view {
    position: absolute; left: 536px; top: 22px; width: 522px; height: 282px;
  }
  .aerial-view svg { width: 100%; height: 100%; display: block; }
  .brand {
    position: absolute; left: 48px; top: 30px;
    display: flex; align-items: center; gap: 10px;
  }
  .brand-mark {
    width: 40px; height: 40px; border-radius: 50%;
    background: var(--brand-blue);
  }
  .brand-name {
    font-family: "Archivo Black", sans-serif;
    font-size: 17px; letter-spacing: 0.5px;
    color: var(--brand-blue);
  }
  .headline {
    position: absolute; left: 40px; top: 94px;
    font-family: "Anton", sans-serif; font-weight: 400;
    font-size: 60px; line-height: 1; letter-spacing: 0.3px;
    white-space: nowrap;
    background: linear-gradient(180deg, var(--brand-blue-light) 0%, var(--brand-blue) 55%, var(--brand-blue-deep) 100%);
    -webkit-background-clip: text; background-clip: text; color: transparent;
  }
  .promo {
    position: absolute; left: 42px; top: 178px;
    display: flex; align-items: center;
  }
  .code-pill {
    display: flex; height: 35px; border-radius: 18px; overflow: hidden;
    font-family: "Archivo Black", sans-serif; font-size: 22px; color: var(--white);
  }
  .code-label {
    display: flex; align-items: center; padding: 0 22px 0 16px;
    background: linear-gradient(180deg, #f0444b 0%, var(--promo-red) 50%, var(--promo-red-deep) 100%);
    border-radius: 18px; position: relative; z-index: 1;
  }
  .code-value {
    display: flex; align-items: center; padding: 0 30px 0 38px;
    background: var(--ink); margin-left: -18px;
  }
  .promo-for {
    font-family: "Oswald", sans-serif; font-weight: 600;
    font-size: 24px; color: var(--ink); margin: 0 10px 0 10px;
  }
  .promo-amount {
    font-family: "Oswald", sans-serif; font-weight: 600;
    color: var(--promo-red); font-size: 62px; line-height: 1;
    display: flex; align-items: flex-start; letter-spacing: -1px;
    margin-top: 4px;
  }
  .promo-amount .currency { font-size: 26px; margin-top: 0; }
  .promo-off {
    font-family: "Oswald", sans-serif; font-weight: 600;
    color: var(--ink); font-size: 42px; line-height: 1; margin-left: 3px;
    margin-top: 6px;
  }
  .website {
    position: absolute; left: 42px; top: 244px;
    font-family: "Michroma", sans-serif; font-size: 22px;
    letter-spacing: 10px; color: var(--ink); white-space: nowrap;
  }
  .website .domain { color: var(--brand-blue); }
</style>
</head>
<body>
  <main class="billboard">
    <div class="sky-backdrop" role="img" aria-label="Sky with sunlit clouds seen from above"></div>

    <div class="aerial-view" role="img" aria-label="Aerial view of a city skyline on the water at sunset, with a passenger's legs and sneakers dangling from a helicopter">
      <svg viewBox="0 0 522 282" preserveAspectRatio="none" aria-hidden="true">
        <defs>
          <linearGradient id="aerial-tone" x1="0" y1="0" x2="0" y2="1">
            <stop offset="0" stop-color="#f1c79a"/>
            <stop offset="0.2" stop-color="#9a8e86"/>
            <stop offset="0.4" stop-color="#3b4a5c"/>
            <stop offset="1" stop-color="#24303e"/>
          </linearGradient>
        </defs>
        <path fill="url(#aerial-tone)"
          d="M70 40 C110 28 160 30 200 26 C230 6 250 16 270 26 C310 20 360 28 410 26 C460 28 505 50 515 80 C522 120 518 165 498 198 C472 236 420 256 360 264 C300 274 240 276 180 268 C120 262 70 246 40 220 C14 196 4 170 14 145 C24 120 40 100 48 80 C54 62 58 48 70 40 Z"/>
      </svg>
    </div>

    <div class="brand">
      <span class="brand-mark"></span>
      <span class="brand-name">HOVERQUILL.COM</span>
    </div>

    <h1 class="headline">Bucket List? Check.</h1>

    <div class="promo">
      <div class="code-pill">
        <span class="code-label">Use Code</span>
        <span class="code-value">YES25</span>
      </div>
      <span class="promo-for">FOR</span>
      <span class="promo-amount"><span class="currency">$</span>25</span>
      <span class="promo-off">OFF</span>
    </div>

    <p class="website">www.<span class="domain">hoverquill</span>.com</p>
  </main>
</body>
</html>
```